Creative, Modern and Conversion based Web Design

Kolvex Digital has recently launched a new logo and as part of our companies rebranding, we need a new website aimed towards the UK B2B marketplace.

The website needs to deliver a modern and creative website design whilst ensuring the design is tailored towards conversion optimisation.

This site must drive point of contact either from an online form, via a direct telephone call or Skype connection.

Our sales are all offline so the website will be a simple, elegant and stunning information portal.

Kolvex Digital offers Digital Marketing services to companies throughout the UK - our target audiences are companies that turnover a minimum of 3 million pounds a year and as such we need to deliver a professional image that installs confidence in our companies abilities.

We do not like websites that are reliant upon stock photography - we are happy for stock photography to be used in a small way however the site must not look like a template filled with stock photography.

What do we do

We supply digital marketing services to those companies who demand a strong return on investment - our company prides itself on delivering successful campaigns that help establish long-term profitable relationships.

A lot of the information presented on our old site is relevant today however the design sucks. So please use the information on our current website as a foundation for your design content.

I am looking for several page designs including

"Home Page" Desktop Version
"Service Page" Desktop Version
"Blog Page" Desktop Version

"Home Page" Mobile Version
"Service Page" Mobile Version
"Blog Page" Mobile Version

In the 1st instance please only submit a single design for the "Home Page" Desktop Version - those designers that we are impressed with will be asked to complete the other designs before a winner is selected.

I like modern clean fonts - the site needs to welcome the reader and encourage them to absorb the information - not to overload and make them leave.

The site must be designed to naturally fit our companies new logo.

NO TEMPLATES

Target Market(s)

B2b - 3 million turnover and above

Industry/Entity Type

Digital Marketing

Number of Pages Required

3 page

Requirements
Must have
• Blended well with the companies logo
• We need conversion optimisation to be a huge part of the design - we considered a conversation when a potential customer reaches out to use via - web form, telephone or skype
• The current content on the old website fits today's business but the design sucks.
• www.kolvexdigital-example.com
Nice to have
• We need 3 pages (in 2 variants Desktop and Mobile)
• Home Page
• Service Page
• Blog Page
• Please only deliver the "Home Page" desktop version - if we are happy with your design we will aks for the additional pages
Should not have
• No templates and not stock photo heavy design

```html
<!DOCTYPE html>
<html lang="en">
<head>
<meta charset="utf-8">
<title>Kolvex Digital – ROI Driven Digital Agency</title>
<link rel="stylesheet" href="https://fonts.googleapis.com/css2?family=Montserrat:wght@400;500;600;700&display=swap">
<style>
:root{
  --navy:#172a6e;
  --navy-deep:#101e52;
  --blue:#2a6fd6;
  --sky:#2f8fe8;
  --purple:#6b3fa8;
  --violet:#8a4cc6;
  --ink:#1c1c1c;
  --grey:#6d6d6d;
  --light:#eceef2;
  --white:#ffffff;
}
*{margin:0;padding:0;box-sizing:border-box}
html,body{width:1200px;height:2548px;overflow:hidden}
body{font-family:"Montserrat",sans-serif;color:var(--ink);background:var(--white);position:relative}

/* Hero */
.hero{position:absolute;left:0;top:0;width:1200px;height:520px;overflow:hidden}
.hero-photo{position:absolute;inset:0;background:
  radial-gradient(ellipse at 30% 30%,rgba(255,255,255,.35),transparent 45%),
  linear-gradient(120deg,#5c7fc4 0%,#4a5fb8 35%,#6a44b0 70%,#3a2f8c 100%)}
.topbar{position:absolute;left:0;top:0;width:100%;height:96px;background:rgba(16,30,82,.55)}
.brand{position:absolute;left:40px;top:16px;display:flex;align-items:center;gap:10px;color:var(--white);font-weight:700;font-size:20px;letter-spacing:.5px}
.brand-mark{width:22px;height:22px;border:2px solid var(--white)}
.contact-row{position:absolute;right:40px;top:18px;display:flex;gap:34px;color:var(--white);font-size:12px;font-weight:500}
.contact-row span{display:flex;align-items:center;gap:8px}
.nav{position:absolute;right:40px;top:60px;display:flex;gap:30px;color:var(--white);font-size:13px;font-weight:600;text-transform:uppercase}
.hero-copy{position:absolute;left:0;top:232px;width:100%;text-align:center;color:var(--white)}
.hero-kicker{font-size:20px;font-weight:500}
.hero-title{display:flex;justify-content:center;align-items:center;gap:20px;font-size:40px;font-weight:700;margin-top:6px;letter-spacing:1px}
.hero-actions{display:flex;justify-content:center;gap:22px;margin-top:38px}
.btn{display:inline-block;padding:12px 26px;border-radius:24px;font-size:13px;font-weight:700;text-transform:uppercase}
.btn-light{background:var(--white);color:var(--navy)}
.btn-outline{border:2px solid var(--white);color:var(--white)}
.btn-sky{background:var(--sky);color:var(--white)}

/* Services */
.services{position:absolute;left:0;top:590px;width:1200px;text-align:center}
.section-title{font-size:36px;font-weight:600}
.title-rule{width:240px;height:2px;background:var(--ink);margin:10px auto 0}
.service-grid{display:grid;grid-template-columns:repeat(3,300px);column-gap:48px;row-gap:58px;justify-content:center;margin-top:54px}
.service{display:flex;flex-direction:column;align-items:center}
.service-icon{width:118px;height:118px;border-radius:50%;background:#111;display:flex;align-items:center;justify-content:center}
.service h3{font-size:22px;font-weight:600;margin-top:18px}
.service p{font-size:12px;line-height:1.5;color:var(--grey);margin-top:8px;width:270px;height:72px}
.service .btn-sky{padding:8px 22px;font-size:11px;margin-top:26px}

/* Stats */
.growth{position:absolute;left:0;top:1470px;width:1200px;height:606px;overflow:hidden}
.growth-photo{position:absolute;inset:0;background:linear-gradient(100deg,var(--purple) 0%,#5a4fb8 45%,var(--blue) 100%)}
.wave{position:absolute;left:0;top:0}
.growth-copy{position:absolute;left:0;top:170px;width:100%;text-align:center;color:var(--white)}
.growth-title{font-size:34px;font-weight:600}
.stats{display:flex;justify-content:center;gap:200px;margin-top:36px}
.stat{width:160px;display:flex;flex-direction:column;align-items:center}
.stat-num{width:92px;height:92px;border-radius:50%;background:var(--sky);border:3px solid var(--white);display:flex;align-items:center;justify-content:center;font-size:26px;font-weight:700}
.stat-label{font-size:20px;font-weight:500;margin-top:14px;white-space:nowrap}
.roi-ask{font-size:22px;margin-top:40px;font-weight:500}
.roi-note{font-size:12px;opacity:.85;margin-top:10px;line-height:1.5}
.growth-copy .btn-sky{margin-top:22px;padding:10px 26px;font-size:11px}

/* Partners */
.partners{position:absolute;left:0;top:2076px;width:1200px;height:104px;background:var(--light);display:flex;align-items:center;justify-content:space-around;padding:0 30px}
.badge{width:150px;height:36px;background:#8c8f96;border-radius:4px}
.badge.round{width:48px;height:48px;border-radius:50%}

/* Footer */
.footer{position:absolute;left:0;top:2180px;width:1200px;height:368px;background:linear-gradient(180deg,var(--navy) 0%,#1f4aa6 100%);color:var(--white)}
.footer-cols{position:absolute;left:176px;top:34px;display:flex;gap:90px}
.footer h4{font-size:20px;font-weight:600;margin-bottom:18px}
.footer ul{list-style:none;font-size:13px;font-weight:600;line-height:2.15}
.footer li::before{content:"›";margin-right:8px}
.office{font-size:13px;line-height:1.75}
.socials{position:absolute;left:176px;top:236px;display:flex;gap:14px}
.socials span{width:26px;height:26px;border-radius:50%;background:var(--white)}
.copyright{position:absolute;left:0;bottom:0;width:100%;height:54px;background:var(--navy-deep);display:flex;align-items:center;justify-content:center;font-size:12px;font-weight:600;letter-spacing:.5px}
</style>
</head>
<body>

<header class="hero">
  <div class="hero-photo" role="img" aria-label="Photo of a hand pointing at a growth chart on a screen, tinted blue and purple"></div>
  <div class="topbar"></div>
  <div class="brand"><span class="brand-mark"></span>Kolvex Digital</div>
  <div class="contact-row">
    <span><svg width="12" height="12" viewBox="0 0 24 24" fill="#fff"><path d="M6.6 10.8a15 15 0 0 0 6.6 6.6l2.2-2.2c.3-.3.7-.4 1-.2 1.1.4 2.3.6 3.6.6.6 0 1 .4 1 1V20c0 .6-.4 1-1 1A17 17 0 0 1 3 4c0-.6.4-1 1-1h3.5c.6 0 1 .4 1 1 0 1.3.2 2.5.6 3.6.1.3 0 .7-.2 1z"/></svg>+44 (0) 7000 482190</span>
    <span><svg width="10" height="13" viewBox="0 0 20 26" fill="#fff"><path d="M10 0a10 10 0 0 0-10 10c0 7.5 10 16 10 16s10-8.5 10-16A10 10 0 0 0 10 0zm0 14a4 4 0 1 1 0-8 4 4 0 0 1 0 8z"/></svg>Shrewsbury Office</span>
  </div>
  <nav class="nav"><span>Home</span><span>Services</span><span>White Link Label Building</span><span>Blog</span></nav>
  <div class="hero-copy">
    <div class="hero-kicker">Search marketing</div>
    <div class="hero-title">
      <svg width="18" height="34" viewBox="0 0 18 34"><path d="M16 2 2 17l14 15" stroke="#fff" stroke-width="3" fill="none"/></svg>
      ROI DRIVEN DIGITAL AGENCY
      <svg width="18" height="34" viewBox="0 0 18 34"><path d="M2 2l14 15L2 32" stroke="#fff" stroke-width="3" fill="none"/></svg>
    </div>
    <div class="hero-actions"><span class="btn btn-light">Get Started</span><span class="btn btn-outline">Contact Us</span></div>
  </div>
</header>

<section class="services">
  <h2 class="section-title">Our Services</h2>
  <div class="title-rule"></div>
  <div class="service-grid">
    <article class="service">
      <div class="service-icon"><svg width="60" height="60" viewBox="0 0 60 60" fill="none" stroke="#fff" stroke-width="5"><circle cx="24" cy="24" r="14"/><path d="M34 34l16 16"/></svg></div>
      <h3>Organic Search</h3>
      <p>Attract steady visitors who already search for what you offer, with content and fixes that lift your rankings month after month.</p>
      <span class="btn btn-sky">Read More</span>
    </article>
    <article class="service">
      <div class="service-icon"><svg width="60" height="60" viewBox="0 0 60 60" fill="none" stroke="#fff" stroke-width="5"><circle cx="24" cy="24" r="14"/><path d="M34 34l16 16M24 17v14M17 24h14"/></svg></div>
      <h3>Paid Search</h3>
      <p>Campaigns built for return, not clicks. We tune bids, ads and landing pages so every pound spent works harder for your sales team.</p>
      <span class="btn btn-sky">Read More</span>
    </article>
    <article class="service">
      <div class="service-icon"><svg width="64" height="64" viewBox="0 0 64 64" fill="none" stroke="#fff" stroke-width="5"><path d="M32 6v52M6 32h52M24 14l8-8 8 8M24 50l8 8 8-8M14 24l-8 8 8 8M50 24l8 8-8 8"/></svg></div>
      <h3>Link Outreach</h3>
      <p>Real links from relevant sites in your sector, earned through honest outreach that builds authority and trust for your domain.</p>
      <span class="btn btn-sky">Read More</span>
    </article>
    <article class="service">
      <div class="service-icon"><svg width="60" height="60" viewBox="0 0 60 60" fill="none" stroke="#fff" stroke-width="5"><path d="M40 8l12 12-28 28H12V36z"/><path d="M10 54h40"/></svg></div>
      <h3>UX &amp; CRO</h3>
      <p>We study how visitors move through your site and remove the friction that stops them, turning more of them into real enquiries.</p>
      <span class="btn btn-sky">Read More</span>
    </article>
    <article class="service">
      <div class="service-icon"><svg width="62" height="62" viewBox="0 0 62 62" fill="none" stroke="#fff" stroke-width="5"><rect x="8" y="14" width="46" height="34"/><path d="M8 14l23 18 23-18"/></svg></div>
      <h3>Email Marketing</h3>
      <p>Clear, well timed emails that keep your brand in view and guide prospects gently from first interest to a signed contract.</p>
      <span class="btn btn-sky">Read More</span>
    </article>
    <article class="service">
      <div class="service-icon"><svg width="60" height="60" viewBox="0 0 60 60" fill="#fff" stroke="#fff" stroke-width="4"><circle cx="16" cy="30" r="7"/><circle cx="44" cy="14" r="7"/><circle cx="44" cy="46" r="7"/><path d="M16 30L44 14M16 30l28 16" fill="none"/></svg></div>
      <h3>Social Media</h3>
      <p>Focused social campaigns that reach decision makers where they spend time, grow your audience and support every other channel.</p>
      <span class="btn btn-sky">Read More</span>
    </article>
  </div>
</section>

<section class="growth">
  <div class="growth-photo" role="img" aria-label="City skyline photo tinted purple and blue"></div>
  <svg class="wave" width="1200" height="150" viewBox="0 0 1200 150" preserveAspectRatio="none"><path d="M0 0H1200V20C1000 110 760 40 560 70 360 100 180 150 0 90Z" fill="#fff"/></svg>
  <div class="growth-copy">
    <h2 class="growth-title">We grow as our clients grow. That’s what we love.</h2>
    <div class="stats">
      <div class="stat"><div class="stat-num">117</div><div class="stat-label">Satisfied Clients</div></div>
      <div class="stat"><div class="stat-num">215</div><div class="stat-label">Campaigns Finished</div></div>
      <div class="stat"><div class="stat-num">1,798</div><div class="stat-label">Cups of Coffee</div></div>
    </div>
    <div class="roi-ask">Want To Improve Your ROI? Let’s Talk</div>
    <div class="roi-note">Book a short call with our team and we will map out<br>where your next gains are hiding.</div>
    <span class="btn btn-sky">Get Started</span>
  </div>
</section>

<section class="partners" aria-label="Partner badges">
  <span class="badge"></span><span class="badge round"></span><span class="badge"></span><span class="badge"></span><span class="badge"></span><span class="badge round"></span>
</section>

<footer class="footer">
  <div class="footer-cols">
    <div>
      <h4>Our Key Services</h4>
      <ul><li>Link Outreach</li><li>Organic Search (SEO)</li><li>Paid Search (PPC)</li><li>Social Media Marketing</li></ul>
    </div>
    <div>
      <h4>Locations We Cover (SEO)</h4>
      <ul><li>Birmingham</li><li>Essex</li><li>London</li><li>Manchester</li><li>Stoke-on-Trent</li><li>See All Locations We Cover (SEO)</li></ul>
    </div>
    <div>
      <h4>Shrewsbury Office</h4>
      <p class="office">Kolvex Digital Ltd<br>The Granary<br>12 Harrow Lane<br>Elm Green<br>Shrewsbury<br>SY1 0ZZ<br><br>Phone: 01700 482190<br>Email: info@kolvexdigital-example.com</p>
    </div>
  </div>
  <div class="socials"><span></span><span></span><span></span><span></span></div>
  <div class="copyright">© 2018 KOLVEX DIGITAL LIMITED. ALL RIGHTS RESERVED.</div>
</footer>

</body>
</html>
```